Create a Graphic About YOURSELF and PixelHarbor

PixelHarbor would like you (designers) to create an awesome graphic to promote YOURSELF and your profile on PixelHarbor!

Your graphic should communicate your name, your services and should mention PixelHarbor.

The design should be perfect for sharing on Chatterly. Here's an example of what we'd like http://blog.pixelharbor-example.ca/article/333/pixelharbor-launches-3000-hire-me-social-design-contest

Once you submitted your design, we'd love you to share the design ('advertisement') and promote yourself and PixelHarbor to your friends and potential customers. So make your submissions great and get your friends to vote for your design by 'Liking' it on Chatterly!

Prizes:
$1500 - "PixelHarbor Community" prize awarded to the designer with the most Chatterly 'Likes'
5 x $50 for the next 5 'most liked' designs on Chatterly

$1000 - "Hire Me" prize awarded to the designer who receives the most client invites
5 x $50 for the next 5 'most invited' designers

In summary, this is a great opportunity for you to increase your exposure to PixelHarbor customers and win cash prizes. Show off your design skills and get hired by PixelHarbor customers from around the world!

Target Market(s)

Fans, friends and customers of YOU

Industry/Entity Type

Cash

Requirements
Must have
• 1) Include your PixelHarbor user name on the graphic so customers can find you in the PixelHarbor Designer Directory
2) Include the tagline "Hire Me on PixelHarbor.com!" in your graphic design.
3) Share your design's URL on our Chatterly wall at http://chatterly-example.com/pixelharbor and get your friends to 'like' your design.
Nice to have
• 1) Include a tagline that expresses your design approach/philosophy
2) Artwork dimensions: 403 x 403 px
3) You can submit more than 1 design!
Should not have
• You must own the copyright of any images you use including stock imagery.

```html
<!DOCTYPE html>
<html lang="en">
<head>
<meta charset="utf-8">
<title>MIRA808 design – PixelHarbor</title>
<link rel="stylesheet" href="https://fonts.googleapis.com/css2?family=Audiowide&family=Open+Sans:wght@600;700&display=swap">
<style>
  :root {
    --kraft-light: #e0bb58;
    --kraft-mid: #d4aa4a;
    --kraft-dark: #bb9035;
    --ornament-core: rgba(30, 20, 8, 0.62);
    --ornament-mid: rgba(40, 28, 10, 0.32);
    --ornament-fade: rgba(40, 28, 10, 0);
    --handle-pink: #f28af0;
    --handle-violet: #c08af4;
    --handle-blue: #7d9ef8;
    --handle-edge: #2e2240;
    --brand-ink: #1b1b1b;
    --brand-blue: #1e6c9c;
    --services-blue: #2874a6;
    --frame: #f4ecd2;
  }
  html, body {
    margin: 0;
    padding: 0;
    width: 1200px;
    height: 750px;
    overflow: hidden;
    background: #ffffff;
  }
  .promo-card {
    display: block;
    width: 1200px;
    height: 750px;
  }
  .handle-text {
    font-family: "Audiowide", sans-serif;
    font-size: 182px;
    fill: url(#handle-fill);
    stroke: var(--handle-edge);
    stroke-width: 5px;
    paint-order: stroke fill;
  }
  .role-text {
    font-family: "Audiowide", sans-serif;
    font-size: 136px;
    fill: url(#handle-fill);
    stroke: var(--handle-edge);
    stroke-width: 4px;
    paint-order: stroke fill;
  }
  .brand-name {
    font-family: "Open Sans", sans-serif;
    font-weight: 600;
    font-size: 106px;
    fill: var(--brand-ink);
  }
  .brand-dot {
    fill: var(--brand-blue);
  }
  .services-line {
    font-family: "Open Sans", sans-serif;
    font-weight: 700;
    font-size: 62px;
    fill: var(--services-blue);
  }
</style>
</head>
<body>
<svg class="promo-card" viewBox="0 0 1200 750" xmlns="http://www.w3.org/2000/svg">
  <defs>
    <radialGradient id="kraft-paper" cx="50%" cy="45%" r="75%">
      <stop offset="0%" stop-color="var(--kraft-light)"/>
      <stop offset="70%" stop-color="var(--kraft-mid)"/>
      <stop offset="100%" stop-color="var(--kraft-dark)"/>
    </radialGradient>
    <radialGradient id="ornament-shade" cx="50%" cy="55%" r="50%">
      <stop offset="0%" stop-color="var(--ornament-core)"/>
      <stop offset="55%" stop-color="var(--ornament-mid)"/>
      <stop offset="100%" stop-color="var(--ornament-fade)"/>
    </radialGradient>
    <linearGradient id="handle-fill" x1="0" y1="0" x2="1" y2="0.4">
      <stop offset="0%" stop-color="var(--handle-pink)"/>
      <stop offset="60%" stop-color="var(--handle-violet)"/>
      <stop offset="100%" stop-color="var(--handle-blue)"/>
    </linearGradient>
  </defs>

  <rect class="paper-background" width="1200" height="750" fill="url(#kraft-paper)" role="img" aria-label="Textured kraft paper background"/>

  <ellipse class="floral-ornament" cx="600" cy="300" rx="590" ry="270" fill="url(#ornament-shade)" role="img" aria-label="Black floral swirl ornament with curling vines, leaves, small flowers and ink splatter spreading behind the name"/>

  <rect class="card-frame" x="3" y="3" width="1194" height="744" fill="none" stroke="var(--frame)" stroke-width="3"/>

  <text class="handle-text" x="68" y="398" textLength="1057" lengthAdjust="spacingAndGlyphs">MIRA808</text>
  <text class="role-text" x="360" y="492" textLength="472" lengthAdjust="spacingAndGlyphs">design</text>

  <circle class="brand-dot" cx="251" cy="585" r="58"/>
  <text class="brand-name" x="338" y="622" textLength="622" lengthAdjust="spacingAndGlyphs">PixelHarbor</text>

  <text class="services-line" x="270" y="705" textLength="660" lengthAdjust="spacingAndGlyphs">brochure website logo</text>
</svg>
</body>
</html>
```